Dental Business Card

I need Dental oriented business cards.
On the front side -
- on the first line, my name:
Dr Marlow Tasker
- on the second line (just underneath):
Doctor of Dental Medicine
- on the third line, or underneath that or in a corner, I would like the address and phone number:
5192 Ch. Birchfield
Montreal QC H2P 4K8
514-629-5074
- other than that i would maybe like a logo of a tooth, but i want it to be subtle and very basic!
- I would like the card to be preferably black or dark grey-ish with the writing in white
On the other side -
- 2-3 lines with the possibility to write the next appointment the box with the lines should be white, with the rest of the card being black

```html
<!DOCTYPE html>
<html lang="en">
<head>
<meta charset="utf-8">
<title>Dr Marlow Tasker – Business Card</title>
<link href="https://fonts.googleapis.com/css2?family=Questrial&display=swap" rel="stylesheet">
<style>
  :root {
    --page-bg: #2a2a2d;
    --card-black: #131313;
    --ink-white: #ffffff;
    --ink-dark: #1a1a1a;
    --accent-magenta: #a24f9c;
    --rule-dark: #222222;
  }
  html, body {
    margin: 0;
    width: 1200px;
    height: 800px;
    overflow: hidden;
    background: var(--page-bg);
    font-family: "Questrial", "Helvetica Neue", Arial, sans-serif;
  }
  .sheet {
    position: relative;
    width: 1200px;
    height: 800px;
    display: flex;
    align-items: center;
    justify-content: center;
    gap: 40px;
  }
  .card {
    position: relative;
    width: 540px;
    height: 320px;
    border-radius: 24px;
    background: var(--card-black);
    box-sizing: border-box;
    overflow: hidden;
  }

  /* Back side: appointment */
  .appointment-panel {
    position: absolute;
    inset: 16px;
    background: var(--ink-white);
    border-radius: 22px;
  }
  .appointment-title {
    position: absolute;
    top: 30px;
    left: 0;
    right: 0;
    text-align: center;
    font-size: 14px;
    letter-spacing: 1px;
    color: var(--ink-dark);
  }
  .appointment-line {
    position: absolute;
    left: 60px;
    right: 40px;
    height: 1px;
    background: var(--rule-dark);
  }
  .appointment-line.first  { top: 110px; }
  .appointment-line.second { top: 170px; }
  .appointment-line.third  { top: 230px; }

  /* Front side */
  .brand {
    position: absolute;
    top: 38px;
    right: 40px;
    display: flex;
    align-items: center;
    gap: 8px;
    color: var(--ink-white);
    font-size: 14px;
    letter-spacing: 0.5px;
  }
  .brand-dot {
    width: 12px;
    height: 12px;
    border-radius: 50%;
    background: var(--accent-magenta);
  }
  .doctor-name {
    position: absolute;
    left: 44px;
    top: 118px;
    margin: 0;
    font-size: 30px;
    font-weight: 400;
    letter-spacing: 0.5px;
    color: var(--ink-white);
  }
  .doctor-title {
    position: absolute;
    left: 46px;
    top: 158px;
    margin: 0;
    font-size: 17px;
    color: var(--accent-magenta);
  }
  .rule {
    position: absolute;
    height: 1px;
  }
  .rule.accent {
    left: 44px;
    top: 238px;
    width: 330px;
    background: var(--accent-magenta);
  }
  .rule.light {
    left: 378px;
    top: 222px;
    width: 122px;
    background: var(--ink-white);
  }
  .phone {
    position: absolute;
    left: 44px;
    top: 252px;
    font-size: 15px;
    letter-spacing: 0.5px;
    color: var(--ink-white);
  }
  .address {
    position: absolute;
    left: 382px;
    top: 232px;
    font-style: normal;
    font-size: 12.5px;
    line-height: 1.5;
    color: var(--ink-white);
  }
</style>
</head>
<body>
  <main class="sheet">
    <section class="card card-back" aria-label="Appointment side">
      <div class="appointment-panel">
        <div class="appointment-title">APPOINTMENT</div>
        <div class="appointment-line first"></div>
        <div class="appointment-line second"></div>
        <div class="appointment-line third"></div>
      </div>
    </section>

    <section class="card card-front" aria-label="Contact side">
      <div class="brand"><span class="brand-dot"></span>Tasker Dental</div>
      <h1 class="doctor-name">DR MARLOW TASKER</h1>
      <p class="doctor-title">Doctor of Dental Medicine</p>
      <div class="rule accent"></div>
      <div class="rule light"></div>
      <div class="phone">514-629-5074</div>
      <address class="address">5192 Ch. Birchfield<br>Montreal QC H2P 4K8</address>
    </section>
  </main>
</body>
</html>
```